The company Velquist needs a design for CBD capsules

We (Velquist) need a new design for our CBD capsules. We already have a design for CBD oil. However, we do not want to use this completely. The Talmbex label and the cans serve as a template. Please upload in the format 139mm x 59mm incl.
2mm bleed all around and in .pdf vector. The logo files for Velquist are included in the briefing.

Industry/Entity Type

Onlineshop

Colors
00AB8E
00BBA5
67D7C9
C6EFE9
E9F9F6

Requirements
Must have
• Please in the format 139mm x 59mm incl. 2mm bleed all around and .pdf vector
Should not have
• It shouldn't be the same label, but it should be recognizable.

```html
<!DOCTYPE html>
<html lang="de">
<head>
<meta charset="utf-8">
<title>Velquist CBD Kapseln – Etikett</title>
<link href="https://fonts.googleapis.com/css2?family=Fraunces:opsz,wght@144,800&family=Montserrat:wght@400;500;700&family=Mrs+Saint+Delafield&display=swap" rel="stylesheet">
<style>
  :root{
    --page-bg:#9e9e9e;
    --label-white:#f7f8f8;
    --band-teal:#2e5866;
    --ink-teal:#2f4f5c;
    --lime:#afc965;
    --lime-dark:#9bbf3f;
    --white:#ffffff;
    --leaf-a:#4f8a2e;
    --leaf-b:#8fc24a;
  }
  *{margin:0;padding:0;box-sizing:border-box}
  html,body{width:1200px;height:900px;overflow:hidden;background:var(--page-bg)}
  .label{
    position:absolute;left:258px;top:40px;width:684px;height:820px;
    background:var(--label-white);overflow:hidden;
    font-family:'Montserrat',sans-serif;color:var(--ink-teal);
  }
  .brand-band{
    position:absolute;left:0;top:0;width:100%;height:248px;background:var(--band-teal);
    display:flex;align-items:center;justify-content:center;padding-top:20px;
  }
  .brand-name{
    font-family:'Fraunces',serif;font-weight:800;font-size:112px;color:var(--white);
    letter-spacing:-1px;line-height:1;
  }
  .product-title{
    position:absolute;left:47px;top:308px;display:flex;align-items:baseline;gap:26px;
  }
  .product-title .cbd{font-weight:700;font-size:132px;line-height:1;letter-spacing:1px}
  .product-title .form{font-weight:400;font-size:50px;line-height:1}
  .rule{position:absolute;left:47px;top:427px;width:534px;height:3px;background:var(--lime)}
  .claims{position:absolute;left:47px;top:505px;list-style:none}
  .claims li{display:flex;align-items:center;gap:8px;font-size:42px;font-weight:500;height:60px}
  .claims svg{width:32px;height:32px;flex:none}
  .product-visual{
    position:absolute;left:451px;top:437px;width:214px;height:243px;border-radius:40px;
    background:radial-gradient(circle at 50% 40%,var(--leaf-b),var(--leaf-a) 70%,transparent 72%);
  }
  .spectrum{
    position:absolute;left:66px;top:660px;font-family:'Mrs Saint Delafield',cursive;
    font-size:70px;line-height:1;color:var(--ink-teal);
  }
  .strength-band{position:absolute;left:0;top:679px;width:684px;height:141px}
  .strength{
    position:absolute;left:498px;top:708px;width:110px;text-align:center;
    font-weight:700;font-size:50px;color:var(--white);line-height:1;
  }
</style>
</head>
<body>
  <div class="label">
    <header class="brand-band">
      <span class="brand-name">Velquist</span>
    </header>

    <div class="product-title">
      <span class="cbd">CBD</span>
      <span class="form">Kapseln</span>
    </div>
    <div class="rule"></div>

    <ul class="claims">
      <li>
        <svg viewBox="0 0 32 32" aria-hidden="true"><circle cx="16" cy="16" r="12" fill="none" stroke="var(--lime-dark)" stroke-width="3"/><path d="M10 16l5 5 13-14" fill="none" stroke="var(--lime-dark)" stroke-width="3.5" stroke-linecap="round" stroke-linejoin="round"/></svg>
        Vegan
      </li>
      <li>
        <svg viewBox="0 0 32 32" aria-hidden="true"><circle cx="16" cy="16" r="12" fill="none" stroke="var(--lime-dark)" stroke-width="3"/><path d="M10 16l5 5 13-14" fill="none" stroke="var(--lime-dark)" stroke-width="3.5" stroke-linecap="round" stroke-linejoin="round"/></svg>
        Gentechnik Frei
      </li>
    </ul>

    <div class="product-visual" role="img" aria-label="Hanfblatt mit grünen Softgel-Kapseln"></div>

    <div class="spectrum">Vollspektrum</div>

    <svg class="strength-band" viewBox="0 0 684 141" aria-hidden="true">
      <path d="M0 99 H412 Q430 99 438 80 L460 18 Q467 0 486 0 H684 V141 H0 Z" fill="var(--lime)"/>
    </svg>
    <div class="strength">10%</div>
  </div>
</body>
</html>
```